Brightmoor Surface Index

I have a current web site that it looking quite aged and it needs a new lease of life. This is a Graffiti Management Website so is all about data processing and management of information. I want a html 5 view on any platform design. clean crisp and new. I have provided some screen shots of my current site.

Target Market(s)

The Target Market will be local government. most users will not be heavy pc users

Industry/Entity Type

Management

Font styles to use
Sans Serif
Other font styles liked:
• web font like calibri

Colors

Designer to choose colors to be used in the design.

Requirements
Must have
• Must have menus similar to attachments

```html
<!DOCTYPE html>
<html lang="en">
<head>
<meta charset="utf-8">
<title>Brightmoor Surface Index</title>
<link href="https://fonts.googleapis.com/css2?family=Open+Sans:wght@400;600;700&display=swap" rel="stylesheet">
<style>
:root{
  --sky:#5aa7dc;
  --sky-light:#7ebbe6;
  --navy:#0b0f6b;
  --ink:#0a1a6e;
  --nav-bg:#e1e1e1;
  --nav-line:#c9c9c9;
  --nav-text:#8a8a8a;
  --hero-bg:#efefef;
  --feature:#5bb5e6;
  --body-text:#4a4a4a;
  --muted:#7b7b7b;
  --footer:#2b2b2b;
  --footer-text:#b9b9b9;
  --white:#ffffff;
}
*{margin:0;padding:0;box-sizing:border-box}
html,body{width:1200px;height:1002px;overflow:hidden}
body{font-family:"Open Sans",Arial,sans-serif;background:var(--white);position:relative}
.masthead{position:absolute;left:0;top:0;width:1200px;height:76px;
  background:linear-gradient(180deg,var(--sky-light),var(--sky))}
.brand{position:absolute;left:0;width:1200px;top:4px;text-align:center;color:var(--white);
  font-weight:700;font-size:52px;letter-spacing:48px;text-indent:48px;line-height:68px}
.brand-band{position:absolute;left:0;top:76px;width:1200px;height:23px;background:var(--navy);
  color:var(--white);text-align:center;font-weight:700;font-size:15px;letter-spacing:3px;line-height:23px}
.main-nav{position:absolute;left:0;top:99px;width:1200px;height:54px;background:var(--nav-bg)}
.main-nav ul{list-style:none;position:absolute;left:101px;top:0;display:flex;height:54px;
  border-left:1px solid var(--nav-line)}
.main-nav li{height:54px;line-height:54px;text-align:center;font-size:15px;color:var(--nav-text);
  border-right:1px solid var(--nav-line)}
.main-nav li.active{background:#ececec;color:var(--ink);font-weight:600}
.hero{position:absolute;left:0;top:153px;width:1200px;height:408px;
  background:radial-gradient(ellipse at 30% 40%,#f8f8f8 0%,var(--hero-bg) 55%,#e4e4e4 100%)}
.hero h1{position:absolute;left:127px;top:110px;font-size:28px;font-weight:600;color:var(--ink);letter-spacing:.2px}
.hero p{position:absolute;left:127px;top:153px;width:404px;font-size:13.5px;line-height:23px;color:var(--body-text)}
.hero-visual{position:absolute;left:700px;top:68px;width:373px;height:305px;border-radius:10px;
  background:linear-gradient(180deg,#d9d9d9 0%,#e8e8e8 100%)}
.slider-dots{position:absolute;left:550px;top:360px;width:101px;height:22px;border-radius:11px;background:#cfcfcf;
  display:flex;justify-content:center;align-items:center;gap:10px}
.slider-dots span{width:10px;height:10px;border-radius:50%;background:var(--white)}
.slider-dots span.on{background:#cfcfcf;border:2px solid var(--white)}
.features{position:absolute;left:0;top:605px;width:1200px;list-style:none}
.feature{position:absolute;width:200px;text-align:center;color:var(--ink);font-size:19px;font-weight:600;line-height:23px}
.feature .badge{width:94px;height:94px;margin:0 auto 10px;border-radius:50%;background:var(--feature);
  display:flex;align-items:center;justify-content:center}
.divider{position:absolute;left:0;top:805px;width:1200px;height:2px;background:#efefef}
.contact{position:absolute;top:830px;left:0;width:1200px;height:60px;font-style:normal}
.contact-item{position:absolute;font-size:13.5px;line-height:23px;color:var(--muted)}
.contact-item svg{position:absolute;left:-37px}
.site-footer{position:absolute;left:0;top:899px;width:1200px;height:103px;background:var(--footer);color:var(--footer-text)}
.footer-nav{position:absolute;left:101px;top:22px;font-size:13.5px;word-spacing:2px}
.footer-nav span{margin:0 8px}
.copyright{position:absolute;left:101px;top:58px;font-size:13px}
.social{position:absolute;left:971px;top:38px;display:flex;gap:10px}
.social span{width:25px;height:25px;border-radius:50%;background:#5d5d5d}
</style>
</head>
<body>
<header class="masthead"><div class="brand">BSI</div></header>
<div class="brand-band">BRIGHTMOOR SURFACE INDEX</div>

<nav class="main-nav">
  <ul>
    <li class="active" style="width:96px">HOME</li>
    <li style="width:132px">PRODUCTS</li>
    <li style="width:116px">REPORTS</li>
    <li style="width:123px">BENEFITS</li>
    <li style="width:143px">LEGISLATION</li>
    <li style="width:144px">CONTACT US</li>
    <li style="width:99px">LOGIN</li>
    <li style="width:147px">DEMO LOGIN</li>
  </ul>
</nav>

<section class="hero">
  <h1>WELCOME TO BSI</h1>
  <p>Donec pretium viverra orci ac convallis. Sed nec varius massa. Nullam scelerisque ullamcorper nunc, vel rutrum odio hendrerit a. Curabitur in ipsum egestas, finibus purus vitae, interdum urna. Praesent sed felis eu nulla feugiat lobortis. Quisque elit eros, dapibus vitae nisi eu, mattis facilisis lorem.</p>
  <div class="hero-visual" role="img" aria-label="Desktop monitor showing a site visits line chart dashboard"></div>
  <div class="slider-dots"><span class="on"></span><span></span><span></span><span></span></div>
</section>

<ul class="features">
  <li class="feature" style="left:93px"><span class="badge">
    <svg width="46" height="46" viewBox="0 0 46 46" fill="none" stroke="#fff" stroke-width="3.5"><circle cx="23" cy="23" r="19"/><ellipse cx="23" cy="23" rx="8" ry="19"/><path d="M4 23h38M7 14h32M7 32h32"/></svg>
  </span>ONLINE<br>DATABASE</li>
  <li class="feature" style="left:297px"><span class="badge">
    <svg width="46" height="46" viewBox="0 0 46 46"><path d="M21 6a18 18 0 1 0 18 20H21z" fill="#fff"/><path d="M25 3v19h19A19 19 0 0 0 25 3z" fill="#fff"/></svg>
  </span>PHOTOGRAPHIC<br>RECORDS</li>
  <li class="feature" style="left:500px"><span class="badge">
    <svg width="46" height="46" viewBox="0 0 46 46"><rect x="4" y="4" width="38" height="38" rx="5" fill="#fff"/><rect x="4" y="12" width="38" height="2" fill="#5bb5e6"/><g fill="none" stroke="#5bb5e6" stroke-width="2"><circle cx="14" cy="23" r="3"/><circle cx="23" cy="23" r="3"/><circle cx="32" cy="23" r="3"/><circle cx="14" cy="33" r="3"/><circle cx="23" cy="33" r="3"/><circle cx="32" cy="33" r="3"/></g></svg>
  </span>ESTIMATED<br>GRAPHS</li>
  <li class="feature" style="left:703px"><span class="badge">
    <svg width="40" height="40" viewBox="0 0 40 40" fill="#fff"><circle cx="29" cy="9" r="6"/><circle cx="10" cy="20" r="6"/><circle cx="29" cy="31" r="6"/><path d="M10 20L29 9M10 20l19 11" stroke="#fff" stroke-width="3"/></svg>
  </span>SHARING</li>
  <li class="feature" style="left:907px"><span class="badge">
    <svg width="44" height="46" viewBox="0 0 44 46"><path d="M8 8h20l8 8v26H8z" fill="#fff" opacity=".75"/><path d="M12 3h18l9 9v27H12z" fill="#fff"/><path d="M18 20h15M18 26h15M18 32h15" stroke="#5bb5e6" stroke-width="2.5"/></svg>
  </span>COMPARISON<br>REPORTING</li>
</ul>

<div class="divider"></div>

<address class="contact">
  <div class="contact-item" style="left:150px;top:0">
    <svg width="24" height="28" viewBox="0 0 24 28" style="top:6px"><rect x="2" y="2" width="20" height="24" fill="none" stroke="#888" stroke-width="2.5"/><path d="M9 2v11l3-3 3 3V2" fill="#888"/></svg>
    Brightmoor Surface Index<br>PO Box 418, Kelmarsh, NSW 2290
  </div>
  <div class="contact-item" style="left:443px;top:11px">
    <svg width="28" height="28" viewBox="0 0 28 28" style="top:-4px;left:-40px"><path d="M4 3l6 0 3 7-4 3c2 4 5 7 9 9l3-4 7 3v6c-13 0-24-11-24-24z" fill="#888"/></svg>
    Phone: (02) 9000 4127
  </div>
  <div class="contact-item" style="left:677px;top:11px">
    <svg width="28" height="28" viewBox="0 0 28 28" style="top:-4px;left:-40px"><rect x="2" y="9" width="6" height="18" fill="#888"/><rect x="10" y="2" width="10" height="8" fill="none" stroke="#888" stroke-width="2"/><rect x="9" y="10" width="17" height="17" fill="#888"/><g fill="#fff"><rect x="12" y="15" width="3" height="3"/><rect x="17" y="15" width="3" height="3"/><rect x="12" y="20" width="3" height="3"/><rect x="17" y="20" width="3" height="3"/></g></svg>
    Fax : (02) 9000 4128
  </div>
  <div class="contact-item" style="left:882px;top:0">
    <svg width="28" height="20" viewBox="0 0 28 20" style="top:12px;left:-40px"><rect width="28" height="20" fill="#888"/><path d="M1 1l13 10L27 1" fill="none" stroke="#fff" stroke-width="1.6"/></svg>
    E-mail : enquiries@bsindex.com.au<br>Support : support@bsindex.com.au
  </div>
</address>

<footer class="site-footer">
  <div class="footer-nav">Home<span>|</span>Products<span>|</span>Reports<span>|</span>Benefits<span>|</span>Legislation<span>|</span>Contact us<span>|</span>Login<span>|</span>Demo Login</div>
  <div class="copyright">Copyright &copy; 2014 &nbsp;Brightmoor Surface Index. &nbsp;All rights reserved.</div>
  <div class="social"><span></span><span></span><span></span><span></span></div>
</footer>
</body>
</html>
```